Pagebook Ads for HOA Law Firm

We need to create certain ads for a Pagebook ads campaign. We are a law firm in Florida that represents homeowners against HOAs. We need to create the following ads:

1. Image Ads Specifications:

File Type: JPG or PNG
Ratio: 1.91:1 to 4:5
Resolution:
a) 1:1 ratio: 1080 x 1080 pixels
b) 4:5 ratio: 1080 x 1350 pixels
Maximum File Size: 30MB
Minimum Width: 600 pixels
Minimum Height:
a) 1:1 ratio: 600 pixels
b) 4:5 ratio: 750 pixels
Key Elements to Include in the Ads:

1) Headline: "HOA Violating Your Rights?"
2) Main Message: "We sue HOAs for Homeowners."
3) Firm Name: Lindqvist Harrow, P.A.
4) Website: www.covenantshieldcounsel.example
5) Phone Number: 1-800-555-0148
6) Florida Bar Compliance Statement: "Serving Homeowners in Florida with our main office in Miami-Dade."
7) Call-to-Action (CTA): Include a strong CTA such as “Contact us today for a consultation!”
8) Tone and Style: Professional yet approachable. The ad should emphasize trust, expertise, and our dedication to homeowners' rights.
9) Branding: Please use our firm's brand colors and fonts. Ensure that our logo is prominently placed within the ad.
10) Image Suggestions: Consider using images of Florida homes, frustrated homeowners, or visuals that evoke trust, protection, and legal authority.

```html
<!DOCTYPE html>
<html lang="en">
<head>
<meta charset="utf-8">
<title>HOA Homeowner Rights Ad – Lindqvist Harrow, P.A.</title>
<link href="https://fonts.googleapis.com/css2?family=Oswald:wght@300;400;600;700&display=swap" rel="stylesheet">
<style>
  :root {
    --navy: #0d1089;
    --panel: #e6e7e9;
    --white: #ffffff;
    --sky-top: #5f9fe0;
    --sky-mid: #8fb5e6;
    --house: #b3a7cf;
    --pool: #3f6fb6;
    --garden: #3b3a44;
    --suits: #4d566a;
  }
  * { box-sizing: border-box; margin: 0; padding: 0; }
  html, body { width: 1200px; height: 1200px; overflow: hidden; }
  body { font-family: "Oswald", "Arial Narrow", sans-serif; background: var(--panel); }

  .ad { position: relative; width: 1200px; height: 1200px; overflow: hidden; }

  .hero-photo {
    position: absolute; inset: 0 0 300px 0;
    background:
      linear-gradient(180deg, var(--sky-top) 0%, var(--sky-mid) 22%, var(--house) 48%, var(--pool) 74%, var(--garden) 100%);
  }
  .attorneys-photo {
    position: absolute; left: 670px; top: 505px; width: 530px; height: 400px;
    background: linear-gradient(180deg, #6a6f80 0%, var(--suits) 60%, #3d4458 100%);
    border-radius: 180px 180px 0 0;
    opacity: .85;
  }
  .panel { position: absolute; inset: 0; }

  .frame { position: absolute; inset: 0; pointer-events: none; }

  .headline {
    position: absolute; left: 104px; top: 118px;
    color: var(--white); font-weight: 600; font-size: 104px; line-height: 96px;
    letter-spacing: -1px; text-transform: uppercase;
  }
  .subline {
    position: absolute; left: 104px; top: 322px;
    color: var(--white); font-weight: 300; font-size: 47px; line-height: 56px;
    letter-spacing: -.5px; text-transform: uppercase;
  }
  .firm-name {
    position: absolute; right: 84px; top: 214px;
    color: var(--white); font-weight: 400; font-size: 26px; letter-spacing: 1px;
    text-transform: uppercase;
  }

  .consult {
    position: absolute; left: 0; right: 0; top: 706px; text-align: center;
    color: var(--navy); font-weight: 400; font-size: 47px; line-height: 56px;
    text-transform: uppercase;
  }
  .cta {
    position: absolute; left: 305px; top: 789px; width: 589px; height: 91px;
    background: var(--navy); border-radius: 46px;
    display: flex; align-items: center; justify-content: center; gap: 26px;
    color: var(--white); font-weight: 700; font-size: 60px; text-transform: uppercase;
    letter-spacing: -.5px;
  }
  .cta svg { width: 70px; height: 70px; }

  .phone {
    position: absolute; left: 0; right: 0; top: 900px;
    display: flex; align-items: center; justify-content: center; gap: 16px;
    color: var(--navy); font-weight: 700; font-size: 72px; line-height: 84px; letter-spacing: -1px;
  }
  .phone svg { width: 68px; height: 68px; }

  .service-area {
    position: absolute; left: 0; right: 0; top: 1008px;
    display: flex; align-items: center; justify-content: center; gap: 10px;
    color: var(--navy); font-weight: 400; font-size: 33px; line-height: 44px;
    text-transform: uppercase; letter-spacing: -.4px;
  }
  .service-area svg { width: 34px; height: 34px; }

  .website {
    position: absolute; left: 0; right: 0; top: 1070px;
    display: flex; align-items: center; justify-content: center; gap: 16px;
    color: var(--navy); font-weight: 600; font-size: 42px; line-height: 60px;
  }
  .website svg { width: 50px; height: 50px; }
</style>
</head>
<body>
<main class="ad">
  <div class="hero-photo" role="img" aria-label="Photograph of a luxury Florida home at dusk with palm trees, a pool and fire bowls"></div>
  <div class="attorneys-photo" role="img" aria-label="Photograph of the firm's two attorneys in suits, smiling"></div>

  <svg class="panel" viewBox="0 0 1200 1200" aria-hidden="true">
    <polygon points="0,837 599,602 1200,842 1200,1200 0,1200" fill="var(--panel)"/>
  </svg>

  <svg class="frame" viewBox="0 0 1200 1200" aria-hidden="true">
    <polyline points="279,1120 54,1120 54,80 1146,80 1146,1120 921,1120" fill="none" stroke="var(--white)" stroke-width="11"/>
  </svg>

  <h1 class="headline">HOA Violating<br>Your Rights?</h1>
  <p class="subline">We sue HOAs for homeowners</p>
  <p class="firm-name">Lindqvist Harrow, P.A.</p>

  <p class="consult">For a consultation!</p>

  <div class="cta">
    <span>Contact us today</span>
    <svg viewBox="0 0 70 70" aria-hidden="true">
      <g stroke="var(--white)" stroke-width="4" stroke-linecap="round">
        <line x1="28" y1="6" x2="28" y2="16"/>
        <line x1="10" y1="24" x2="20" y2="24"/>
        <line x1="14" y1="10" x2="20" y2="16"/>
        <line x1="42" y1="10" x2="36" y2="16"/>
        <line x1="14" y1="38" x2="20" y2="32"/>
      </g>
      <path d="M27 25 L62 45 L48 48 L58 60 L52 65 L42 53 L34 63 Z" fill="var(--white)"/>
    </svg>
  </div>

  <div class="phone">
    <svg viewBox="0 0 68 68" aria-hidden="true">
      <circle cx="34" cy="34" r="34" fill="var(--navy)"/>
      <path d="M22 17 c3-2 6-1 7 2 l3 7 c1 2 0 4-2 5 l-3 2 c2 5 6 9 11 11 l2-3 c1-2 3-3 5-2 l7 3 c3 1 4 4 2 7 l-3 3 c-4 4-12 2-20-6 s-10-16-6-20 z" fill="var(--white)"/>
    </svg>
    <span>1-800-555-0148</span>
  </div>

  <p class="service-area">
    <svg viewBox="0 0 34 34" aria-hidden="true">
      <circle cx="17" cy="17" r="16" fill="var(--navy)"/>
      <path d="M17 7 a7 7 0 0 1 7 7 c0 5-7 13-7 13 s-7-8-7-13 a7 7 0 0 1 7-7 z" fill="var(--white)"/>
      <circle cx="17" cy="14" r="2.8" fill="var(--navy)"/>
    </svg>
    <span>Serving homeowners in Florida with our main office in Miami-Dade</span>
  </p>

  <p class="website">
    <svg viewBox="0 0 50 50" aria-hidden="true">
      <g fill="none" stroke="var(--navy)" stroke-width="3">
        <circle cx="25" cy="25" r="22"/>
        <ellipse cx="25" cy="25" rx="10" ry="22"/>
        <line x1="25" y1="3" x2="25" y2="47"/>
        <line x1="3" y1="25" x2="47" y2="25"/>
        <path d="M7 13 h36 M7 37 h36"/>
      </g>
    </svg>
    <span>www.covenantshieldcounsel.example</span>
  </p>
</main>
</body>
</html>
```